ALL TEXT Social Media Graphics

We are looking for a series of social media graphics for Instagram (new size: 4:5 (1080 x 1350 pixels) ratio that are ALL TEXT. We want the following quotes below on each graphic; one quote per graphic. AND, In very small letters at the bottom of each graphic, add @PaulaWrenLive
The look and feel of these graphics should be complimentary to the color palette attached below; but keep them simple. But the design is up to you; at the end of this document, I provided various samples of all text graphics that I like as examples.
The Quotes are in the attached WORD document
women trying to lose weight

```html
<!DOCTYPE html>
<html lang="en">
<head>
<meta charset="utf-8">
<title>Golden Summer Slimdown – Social Quote Series</title>
<link rel="stylesheet" href="https://fonts.googleapis.com/css2?family=Anton&family=Bowlby+One+SC&family=Roboto:ital,wght@1,400;1,500&family=Poppins:ital,wght@1,700&display=swap">
<style>
  :root {
    --backdrop: #170010;
    --frame: #ffffff;
    --card: #fbdfe4;
    --berry: #b0135a;
    --rose: #ec5a92;
  }
  * { box-sizing: border-box; margin: 0; padding: 0; }
  html, body { width: 1200px; height: 627px; overflow: hidden; background: var(--backdrop); }
  .series { position: relative; width: 1200px; height: 627px; }
  .post {
    position: absolute; width: 220px; height: 275px;
    background: var(--frame);
  }
  .post__card {
    position: absolute; left: 11px; right: 11px; top: 6px; bottom: 6px;
    background: var(--card); border-radius: 21px;
  }
  .quote {
    position: absolute; left: 0; right: 0; top: 14px; height: 224px;
    display: flex; flex-direction: column; align-items: center; justify-content: center;
    text-align: center; line-height: 1.02;
  }
  .quote span { display: block; white-space: nowrap; }
  .lead { font-family: "Anton", sans-serif; color: var(--berry); letter-spacing: -0.01em; }
  .punch { font-family: "Bowlby One SC", sans-serif; color: var(--rose); }
  .call { font-family: "Roboto", sans-serif; font-style: italic; color: var(--berry); }
  .handle {
    position: absolute; left: 0; right: 0; bottom: 14px; text-align: center;
    font-family: "Poppins", sans-serif; font-style: italic; font-weight: 700;
    font-size: 8.5px; color: var(--berry);
  }
  .c1 { left: 15px; } .c2 { left: 252px; } .c3 { left: 489px; } .c4 { left: 725px; } .c5 { left: 962px; }
  .r1 { top: 20px; } .r2 { top: 326px; }
</style>
</head>
<body>
<main class="series">

  <article class="post c1 r1"><div class="post__card">
    <p class="quote">
      <span class="lead" style="font-size:17px">YOU CAN ABSOLUTELY BE</span>
      <span class="lead" style="font-size:17px">DOWN 20–30 POUNDS</span>
      <span class="lead" style="font-size:18px">BY END OF SUMMER.</span>
      <span class="punch" style="font-size:17px">ALL IT TAKES IS</span>
      <span class="punch" style="font-size:13px">THE RIGHT PLAN–AND</span>
      <span class="punch" style="font-size:15px">YOU'VE FOUND IT.</span>
      <span class="call" style="font-size:13px">COMMENT “GOLDEN” FOR</span>
      <span class="call" style="font-size:12px">THE GOLDEN SUMMER</span>
      <span class="call" style="font-size:26px;font-weight:500">SLIMDOWN!</span>
    </p>
    <p class="handle">@PaulaWrenLive</p>
  </div></article>

  <article class="post c2 r1"><div class="post__card">
    <p class="quote">
      <span class="lead" style="font-size:20px">You've got 8 weeks</span>
      <span class="lead" style="font-size:20px">and the perfect plan</span>
      <span class="lead" style="font-size:20px">to drop 30 pounds.</span>
      <span class="punch" style="font-size:12px">LET'S GET SNATCHED</span>
      <span class="punch" style="font-size:12px">THIS SUMMER WITH</span>
      <span class="punch" style="font-size:17px">THE GOLDEN</span>
      <span class="punch" style="font-size:11px">SUMMER SLIMDOWN.</span>
      <span class="call" style="font-size:16px">Comment “Summer”!</span>
    </p>
    <p class="handle">@PaulaWrenLive</p>
  </div></article>

  <article class="post c3 r1"><div class="post__card">
    <p class="quote">
      <span class="lead" style="font-size:20px">Don't wait 'til next</span>
      <span class="lead" style="font-size:17px">summer to get right.</span>
      <span class="punch" style="font-size:21px">THE TIME IS</span>
      <span class="punch" style="font-size:11px">NOW. DROP 30 POUNDS</span>
      <span class="punch" style="font-size:23px">WITH THE</span>
      <span class="punch" style="font-size:13px">GOLDEN SUMMER</span>
      <span class="punch" style="font-size:21px">SLIMDOWN.</span>
      <span class="call" style="font-size:15px">Comment “Summer”!</span>
    </p>
    <p class="handle">@PaulaWrenLive</p>
  </div></article>

  <article class="post c4 r1"><div class="post__card">
    <p class="quote">
      <span class="lead" style="font-size:18px">Sis, we're dropping</span>
      <span class="lead" style="font-size:17px">belly flat and saying</span>
      <span class="lead" style="font-size:17px">goodbye to stubborn</span>
      <span class="lead" style="font-size:40px">pounds.</span>
      <span class="punch" style="font-size:16px">JOIN THE</span>
      <span class="punch" style="font-size:15px">GOLDEN SUMMER</span>
      <span class="call" style="font-size:15px">Slimdown—comment</span>
      <span class="call" style="font-size:27px;font-weight:500">“Summer”!</span>
    </p>
    <p class="handle">@PaulaWrenLive</p>
  </div></article>

  <article class="post c5 r1"><div class="post__card">
    <p class="quote">
      <span class="lead" style="font-size:19px">Nothing feels better</span>
      <span class="lead" style="font-size:18px">than seeing that scale</span>
      <span class="lead" style="font-size:18px">drop week after week.</span>
      <span class="punch" style="font-size:14px">LET'S LOSE UP TO</span>
      <span class="punch" style="font-size:15px">30 POUNDS THIS</span>
      <span class="punch" style="font-size:11px">SUMMER–TOGETHER.</span>
      <span class="call" style="font-size:14px">Comment “Summer” to</span>
      <span class="call" style="font-size:13px">join the Golden Summer</span>
      <span class="call" style="font-size:29px;font-weight:500">Slimdown!</span>
    </p>
    <p class="handle">@PaulaWrenLive</p>
  </div></article>

  <article class="post c1 r2"><div class="post__card">
    <p class="quote">
      <span class="lead" style="font-size:18px">Snatched waist,</span>
      <span class="lead" style="font-size:25px">flat tummy,</span>
      <span class="punch" style="font-size:16px">30 POUNDS</span>
      <span class="punch" style="font-size:11px">LIGHTER–THAT'S</span>
      <span class="punch" style="font-size:18px">WHAT THE</span>
      <span class="punch" style="font-size:11px">GOLDEN SUMMER</span>
      <span class="punch" style="font-size:17px">SLIMDOWN</span>
      <span class="punch" style="font-size:16px">CHALLENGE</span>
      <span class="punch" style="font-size:18px">DELIVERS.</span>
      <span class="call" style="font-size:14px">Comment “Golden”</span>
      <span class="call" style="font-size:17px">to get the plan</span>
    </p>
    <p class="handle">@PaulaWrenLive</p>
  </div></article>

  <article class="post c2 r2"><div class="post__card">
    <p class="quote">
      <span class="lead" style="font-size:23px">There's still time</span>
      <span class="lead" style="font-size:16px">to drop the 30 pounds</span>
      <span class="lead" style="font-size:16px">and slay this summer.</span>
      <span class="punch" style="font-size:17px">THE GOLDEN</span>
      <span class="punch" style="font-size:27px">SUMMER</span>
      <span class="punch" style="font-size:13px">SLIMDOWN HAS</span>
      <span class="punch" style="font-size:13px">THE BLUEPRINT.</span>
      <span class="call" style="font-size:16px">Comment “Golden”!</span>
    </p>
    <p class="handle">@PaulaWrenLive</p>
  </div></article>

  <article class="post c3 r2"><div class="post__card">
    <p class="quote">
      <span class="lead" style="font-size:19px">If your goal is a tiny</span>
      <span class="lead" style="font-size:24px">waist, flat belly,</span>
      <span class="punch" style="font-size:14px">AND 30 POUNDS</span>
      <span class="punch" style="font-size:13px">DOWN–THIS IS</span>
      <span class="punch" style="font-size:21px">THE PLAN.</span>
      <span class="call" style="font-size:16px">Comment “Summer”</span>
      <span class="call" style="font-size:17px">to join the Golden</span>
      <span class="call" style="font-size:16px">Summer Slimdown!</span>
    </p>
    <p class="handle">@PaulaWrenLive</p>
  </div></article>

  <article class="post c4 r2"><div class="post__card">
    <p class="quote">
      <span class="lead" style="font-size:19px">THIS SUMMER AIN'T</span>
      <span class="lead" style="font-size:19px">OVER—AND NEITHER</span>
      <span class="lead" style="font-size:16px">ARE YOUR BODY GOALS.</span>
      <span class="punch" style="font-size:13px">DROP 30 POUNDS</span>
      <span class="punch" style="font-size:24px">WITH THE</span>
      <span class="punch" style="font-size:14px">GOLDEN SUMMER</span>
      <span class="punch" style="font-size:20px">SLIMDOWN.</span>
      <span class="call" style="font-size:12px">COMMENT “GOLDEN” TO</span>
      <span class="call" style="font-size:21px;font-weight:500">GET THE PLAN</span>
    </p>
    <p class="handle">@PaulaWrenLive</p>
  </div></article>

  <article class="post c5 r2"><div class="post__card">
    <p class="quote">
      <span class="lead" style="font-size:24px">You don't need</span>
      <span class="lead" style="font-size:16px">another diet—you need</span>
      <span class="lead" style="font-size:17px">a system that works.</span>
      <span class="punch" style="font-size:13px">DROP 30 POUNDS</span>
      <span class="punch" style="font-size:24px">WITH THE</span>
      <span class="punch" style="font-size:14px">GOLDEN SUMMER</span>
      <span class="punch" style="font-size:20px">SLIMDOWN.</span>
      <span class="call" style="font-size:15px">Comment “Summer”</span>
      <span class="call" style="font-size:23px;font-weight:500">to start now.</span>
    </p>
    <p class="handle">@PaulaWrenLive</p>
  </div></article>

</main>
</body>
</html>
```